business card for Franco-Turkish restaurant

We are a Franco-Turkish restaurant, Le Mirandel, based in the Cotes d'Armor in Brittany, near the Pink Granite Coast. We serve mainly Turkish cuisine. We would like a card reminding Britain and Turkey. No flag. Color: turquoise (sea ..), green, red. There should be a space for 3 lines: name, address, phone / email

Industry/Entity Type

Fast Food Restaurant

Contact Information for Business Card

Dalbayrak Emrul
Addresse: 14 Rue Paul-Henri Duvic, 22450 Kervalhec, France
Tel:+33 2 96 47 08 39

Colors
33a6d7
f04a50
acd036

Requirements
Nice to have
• Symbols of Britain and Turkey
Should not have
• No flags

```html
<!DOCTYPE html>
<html lang="fr">
<head>
<meta charset="utf-8">
<title>Le Mirandel – carte de visite</title>
<link rel="stylesheet" href="https://fonts.googleapis.com/css2?family=Open+Sans:wght@400;600;700&display=swap">
<style>
  :root {
    --backdrop: #e9e6e2;
    --paper: #f4f4f4;
    --green: #68c94c;
    --turquoise: #3fe1d2;
    --sea: #33a6d7;
    --red: #f04a50;
    --ink: #333333;
    --ghost: #ebebeb;
    --white: #ffffff;
  }
  * { box-sizing: border-box; margin: 0; padding: 0; }
  html, body {
    width: 1200px;
    height: 1200px;
    overflow: hidden;
  }
  body {
    background: var(--backdrop);
    font-family: "Open Sans", Arial, sans-serif;
    position: relative;
  }
  .card {
    position: absolute;
    left: 240px;
    width: 720px;
    height: 435px;
    background: var(--paper);
    overflow: hidden;
  }
  .card--front { top: 105px; }
  .card--back { top: 630px; }

  .card__art {
    position: absolute;
    inset: 0;
    width: 720px;
    height: 435px;
  }

  .holder {
    position: absolute;
    left: 0;
    width: 382px;
    top: 116px;
    text-align: center;
  }
  .holder__name {
    font-size: 38px;
    font-weight: 400;
    color: var(--ink);
    letter-spacing: -0.5px;
    line-height: 1.1;
    white-space: nowrap;
  }
  .holder__role {
    margin-top: 10px;
    font-size: 14px;
    color: var(--red);
    text-transform: uppercase;
    letter-spacing: 0.5px;
  }

  .brand {
    position: absolute;
    text-align: center;
    color: var(--ink);
    font-weight: 400;
  }
  .brand--front {
    left: 382px;
    width: 338px;
    top: 134px;
    font-size: 20px;
  }
  .brand--back {
    left: 0;
    width: 720px;
    top: 262px;
    font-size: 27px;
  }

  .contact {
    position: absolute;
    left: 500px;
    width: 210px;
    color: var(--white);
    font-weight: 600;
    font-size: 16px;
    line-height: 1.25;
    display: flex;
    align-items: center;
  }
  .contact--address { top: 192px; height: 60px; font-size: 14px; }
  .contact--phone { top: 267px; height: 63px; }
  .contact--web { top: 342px; height: 63px; }

  .footer-band {
    position: absolute;
    left: 0;
    bottom: 0;
    width: 720px;
    height: 60px;
    background: var(--green);
    color: var(--white);
    font-weight: 600;
    font-size: 18px;
    display: flex;
    align-items: center;
    justify-content: center;
    letter-spacing: 0.3px;
  }
</style>
</head>
<body>

  <section class="card card--front">
    <svg class="card__art" viewBox="0 0 720 435" aria-hidden="true">
      <circle cx="97" cy="292" r="100" fill="none" stroke="var(--ghost)" stroke-width="12"/>
      <rect x="382" y="0" width="338" height="435" fill="var(--green)"/>
      <circle cx="555" cy="80" r="40" fill="none" stroke="var(--white)" stroke-width="6"/>
      <rect x="382" y="192" width="338" height="60" fill="var(--turquoise)"/>
      <rect x="382" y="267" width="338" height="63" fill="var(--turquoise)"/>
      <rect x="382" y="342" width="338" height="63" fill="var(--turquoise)"/>
      <polygon points="382,192 404,222 382,252" fill="var(--paper)"/>
      <polygon points="382,267 404,298 382,330" fill="var(--paper)"/>
      <polygon points="382,342 404,373 382,405" fill="var(--paper)"/>
      <!-- sea wave and red accent strip -->
      <path d="M382 420 q14 -8 28 0 t28 0 t28 0 t28 0 t28 0 t28 0 t28 0 t28 0 t28 0 t28 0 t28 0 t28 0" fill="none" stroke="var(--sea)" stroke-width="3"/>
      <rect x="382" y="429" width="338" height="6" fill="var(--red)"/>
      <!-- house icon -->
      <polygon points="460,208 446,221 450,221 450,238 470,238 470,221 474,221" fill="var(--red)"/>
      <rect x="457" y="228" width="6" height="10" fill="var(--turquoise)"/>
      <!-- phone icon -->
      <path d="M453 288 c-3 0 -5 3 -4 6 c3 9 10 16 19 19 c3 1 6 -1 6 -4 l0 -3 l-6 -3 l-3 3 c-4 -2 -7 -5 -9 -9 l3 -3 l-3 -6 z" fill="var(--red)"/>
      <!-- globe icon -->
      <circle cx="461" cy="373" r="11" fill="var(--red)"/>
      <ellipse cx="461" cy="373" rx="4.5" ry="11" fill="none" stroke="var(--turquoise)" stroke-width="2"/>
      <line x1="450" y1="373" x2="472" y2="373" stroke="var(--turquoise)" stroke-width="2"/>
    </svg>

    <div class="holder">
      <h1 class="holder__name">Dalbayrak Emrul</h1>
      <p class="holder__role">General Manager</p>
    </div>

    <p class="brand brand--front">Le Mirandel</p>

    <p class="contact contact--address">14 Rue Paul-Henri Duvic,<br>22450 Kervalhec</p>
    <p class="contact contact--phone">+33 2 96 47 08 39</p>
    <p class="contact contact--web">www.le-mirandel.fr</p>
  </section>

  <section class="card card--back">
    <svg class="card__art" viewBox="0 0 720 435" aria-hidden="true">
      <circle cx="360" cy="157" r="72" fill="none" stroke="var(--green)" stroke-width="9"/>
      <path d="M0 352 q20 -9 40 0 t40 0 t40 0 t40 0 t40 0 t40 0 t40 0 t40 0 t40 0 t40 0 t40 0 t40 0 t40 0 t40 0 t40 0 t40 0 t40 0 t40 0" fill="none" stroke="var(--sea)" stroke-width="3"/>
      <rect x="0" y="367" width="720" height="8" fill="var(--red)"/>
    </svg>
    <p class="brand brand--back">Le Mirandel</p>
    <div class="footer-band">www.le-mirandel.fr</div>
  </section>

</body>
</html>
```